Trovadel Ltda

Logo design focused on: - Construction of civil works - Electrical services - Metal structures - Equipment rental Tomas Ibarra Luque Manager trovadel.ltda@norvexmail.com 56 9 41827035 Quirobamba s / n, Tolvas, San Elicio de Varanco

Target Market(s)

Building

Colors
33a6d7
0292cd
33b8a4
0555a3

```html
<!DOCTYPE html>
<html lang="es">
<head>
<meta charset="utf-8">
<title>Trovadel Ltda – Tarjeta de presentación</title>
<link href="https://fonts.googleapis.com/css2?family=Roboto:wght@300;400;500;700&display=swap" rel="stylesheet">
<style>
  :root {
    --sky: #33a6d7;
    --ocean: #0292cd;
    --teal: #33b8a4;
    --navy: #0555a3;
    --ink: #4a4a4a;
    --paper: #ffffff;
    --backdrop: #e9ecef;
  }
  html, body {
    margin: 0;
    width: 1200px;
    height: 1023px;
    overflow: hidden;
    background: var(--backdrop);
    font-family: "Roboto", Arial, sans-serif;
  }
  .business-card {
    position: absolute;
    left: 150px;
    top: 252px;
    width: 900px;
    height: 520px;
    border-radius: 22px;
    overflow: hidden;
    background: linear-gradient(160deg, #ffffff 0%, #f1f2f3 100%);
    box-shadow: 0 10px 30px rgba(0,0,0,0.15);
  }
  .swoosh {
    position: absolute;
    inset: 0;
  }
  .brand {
    position: absolute;
    left: 56px;
    top: 232px;
    display: flex;
    align-items: center;
    gap: 18px;
  }
  .brand-dot {
    width: 64px;
    height: 64px;
    border-radius: 50%;
    background: var(--ocean);
  }
  .brand-name {
    font-size: 40px;
    font-weight: 400;
    color: var(--ocean);
    letter-spacing: 1px;
  }
  .divider {
    position: absolute;
    left: 448px;
    top: 70px;
    width: 1.5px;
    height: 320px;
    background: var(--ocean);
  }
  .contact {
    position: absolute;
    left: 478px;
    top: 62px;
    color: var(--ink);
  }
  .contact-name {
    margin: 0;
    font-size: 38px;
    font-weight: 500;
    color: var(--sky);
    line-height: 1.1;
  }
  .contact-role {
    margin: 2px 0 14px;
    font-size: 19px;
    font-weight: 400;
  }
  .contact-line {
    margin: 0;
    font-size: 18px;
    font-weight: 300;
    line-height: 25px;
  }
  .contact-icon-line {
    display: flex;
    align-items: center;
    gap: 8px;
  }
  .contact-icon { width: 14px; height: 14px; flex: none; }
  .services {
    list-style: none;
    margin: 12px 0 0;
    padding: 0;
  }
  .services li {
    display: flex;
    align-items: center;
    gap: 10px;
    font-size: 18px;
    font-weight: 300;
    line-height: 26px;
  }
  .services li::before {
    content: "";
    width: 9px;
    height: 9px;
    border-radius: 50%;
    background: var(--ocean);
    flex: none;
  }
</style>
</head>
<body>
  <article class="business-card">
    <svg class="swoosh" viewBox="0 0 900 520" preserveAspectRatio="none" aria-hidden="true">
      <defs>
        <linearGradient id="swooshBlue" x1="0" y1="1" x2="1" y2="0">
          <stop offset="0" stop-color="var(--navy)"/>
          <stop offset="0.6" stop-color="var(--ocean)"/>
          <stop offset="1" stop-color="var(--sky)"/>
        </linearGradient>
      </defs>
      <path d="M0,500 C360,505 760,450 900,150 L900,520 L0,520 Z" fill="var(--teal)"/>
      <path d="M0,512 C370,512 770,462 900,168 L900,520 L0,520 Z" fill="#ffffff"/>
      <path d="M80,520 C420,515 790,470 900,182 L900,520 Z" fill="url(#swooshBlue)"/>
    </svg>

    <div class="brand">
      <span class="brand-dot"></span>
      <span class="brand-name">Trovadel Ltda</span>
    </div>

    <div class="divider"></div>

    <section class="contact">
      <h1 class="contact-name">Tomas Ibarra Luque</h1>
      <p class="contact-role">Manager</p>
      <p class="contact-line">Quirobamba s / n, Tolvas,</p>
      <p class="contact-line">San Elicio de Varanco</p>
      <p class="contact-line contact-icon-line">
        <svg class="contact-icon" viewBox="0 0 16 16" aria-hidden="true"><path d="M4 1 L6.5 4.5 L5 6.5 C6 8.5 7.5 10 9.5 11 L11.5 9.5 L15 12 L13 15 C7 14.5 1.5 9 1 3 Z" fill="var(--ocean)"/></svg>
        56 9 41827035
      </p>
      <p class="contact-line contact-icon-line">
        <svg class="contact-icon" viewBox="0 0 16 16" aria-hidden="true"><rect x="1" y="3" width="14" height="10" fill="none" stroke="var(--ocean)" stroke-width="1.6"/><path d="M1 3 L8 9 L15 3" fill="none" stroke="var(--ocean)" stroke-width="1.6"/></svg>
        trovadel.ltda@norvexmail.com
      </p>
      <ul class="services">
        <li>Construcción de OO. CC.</li>
        <li>Estructuras Metálicas</li>
        <li>Servicios Eléctricos</li>
        <li>Arriendo de Equipos</li>
      </ul>
    </section>
  </article>
</body>
</html>
```